Investment company needing business card

We are wanting a business card which looks sharp and easy on the eye. We are thinking of having a business card with the logo embossed on it, to really make it stand out. We will only have a small amount of information of the business card, person's name, position, email address and phone number

Contact Information for Business Card

Danica Pruett
Executive Assistant
+64 21 547 3162
danicap@harwellcapital.co.nz

Requirements
Must have
• Embossed logo
Should not have
• Not to be busy

```html
<!DOCTYPE html>
<html lang="en">
<head>
<meta charset="utf-8">
<title>Harwell Capital – Business Card</title>
<link rel="stylesheet" href="https://fonts.googleapis.com/css2?family=Montserrat:wght@400;600;700&display=swap">
<style>
  :root {
    --page-bg: #eceeed;
    --card-white: #ffffff;
    --brand-green: #27b36f;
    --icon-green: #1f9a5d;
    --brand-grey: #636466;
    --text-white: #ffffff;
  }
  * { margin: 0; padding: 0; box-sizing: border-box; }
  html, body {
    width: 1200px;
    height: 840px;
    overflow: hidden;
    background: var(--page-bg);
    font-family: "Montserrat", sans-serif;
  }
  .canvas {
    width: 1200px;
    height: 840px;
    display: flex;
    align-items: center;
    justify-content: center;
  }
  .business-card {
    position: relative;
    width: 900px;
    height: 514px;
    background: var(--card-white);
    overflow: hidden;
    box-shadow: 0 6px 24px rgba(0,0,0,0.10);
  }
  .card-bands {
    position: absolute;
    inset: 0;
  }
  .brand {
    position: absolute;
    left: 72px;
    top: 128px;
    display: flex;
    align-items: center;
    gap: 18px;
  }
  .brand-square {
    width: 58px;
    height: 58px;
    background: var(--brand-green);
  }
  .brand-name {
    font-weight: 700;
    font-size: 42px;
    letter-spacing: 1px;
    color: var(--brand-green);
    text-transform: uppercase;
    line-height: 1;
  }
  .contact {
    position: absolute;
    left: 72px;
    top: 318px;
  }
  .contact-row {
    display: flex;
    align-items: center;
    height: 46px;
    color: var(--text-white);
    font-size: 19px;
  }
  .contact-icon {
    width: 34px;
    height: 34px;
    background: var(--icon-green);
    display: flex;
    align-items: center;
    justify-content: center;
    margin-right: 26px;
    flex: none;
  }
  .contact-icon svg { width: 20px; height: 20px; }
  .person-name { font-weight: 700; }
  .person-role { font-weight: 400; }
</style>
</head>
<body>
<main class="canvas">
  <section class="business-card">
    <svg class="card-bands" viewBox="0 0 900 514" preserveAspectRatio="none" aria-hidden="true">
      <path d="M0 296 H670 Q686 296 692 280 L705 246 Q710 234 724 234 H900 V514 H0 Z" fill="var(--brand-green)"/>
      <path d="M712 234 L718 218 Q723 206 737 206 H900 V234 Z" fill="var(--brand-grey)"/>
    </svg>

    <div class="brand">
      <span class="brand-square"></span>
      <span class="brand-name">Harwell Capital</span>
    </div>

    <div class="contact">
      <div class="contact-row">
        <span class="contact-icon">
          <svg viewBox="0 0 20 20"><circle cx="10" cy="6" r="4" fill="#fff"/><path d="M2 19 Q2 11 10 11 Q18 11 18 19 Z" fill="#fff"/></svg>
        </span>
        <span><span class="person-name">Danica Pruett</span><span class="person-role"> - Executive Assistant</span></span>
      </div>
      <div class="contact-row">
        <span class="contact-icon">
          <svg viewBox="0 0 20 20"><rect x="5" y="1.5" width="10" height="17" rx="1.5" fill="none" stroke="#fff" stroke-width="1.4"/><line x1="8.5" y1="16" x2="11.5" y2="16" stroke="#fff" stroke-width="1.2"/></svg>
        </span>
        <span>+64 21 547 3162</span>
      </div>
      <div class="contact-row">
        <span class="contact-icon">
          <svg viewBox="0 0 20 20"><rect x="2" y="4.5" width="16" height="11" fill="none" stroke="#fff" stroke-width="1.4"/><path d="M2 4.5 L10 11 L18 4.5" fill="none" stroke="#fff" stroke-width="1.4"/></svg>
        </span>
        <span>danicap@harwellcapital.co.nz</span>
      </div>
    </div>
  </section>
</main>
</body>
</html>
```